Brightvale Energy International Website

Brightvale Energy – Lighting the Path of
UK Homes Sustainably.

New Launch Website

Focus on 4 Product Categories

- Energy PV
- Battery Energy Storage
- EV Charging
- Heat Pumps

Add

Energy News
Enquire Now button Top right every page
Contact us page

Follow Lumenhaus.co.uk for similar content pages

Target Market(s)

Residential home owners UK NOT US

Industry/Entity Type

Energy energy, home energy , EV charging

Coding

Coded - Design and coding required

Number of Pages Required

5+ page

Font styles to use
Sans Serif

Colors
0054AA
0677BA
7BADD7
CADEEF
E8F1F8
59FF00
82FF00
B8FF75
E3FFCB
F4FFEA
FFF300
FFF600
FEFA6F
FFFEC7
FFFEE8

Requirements
Must have
• Strong brand logo on every page, clear content bar
Nice to have
• Add these logos from LumenHaus.co.uk

```html
<!DOCTYPE html>
<html lang="en">
<head>
<meta charset="utf-8">
<title>Brightvale Energy – Home</title>
<link href="https://fonts.googleapis.com/css2?family=Roboto:wght@400;500;700&display=swap" rel="stylesheet">
<style>
:root{
  --blue-deep:#0054AA;
  --blue:#0677BA;
  --blue-mid:#7BADD7;
  --blue-soft:#CADEEF;
  --blue-pale:#E0EAF6;
  --blue-wash:#E8F1F8;
  --yellow:#FFF300;
  --ink:#1d1d1f;
  --grey:#8a9aa8;
  --line:#d6dde4;
  --white:#ffffff;
}
*{box-sizing:border-box;margin:0;padding:0}
html,body{width:1200px;height:3075px;overflow:hidden}
body{font-family:'Roboto',sans-serif;color:var(--ink);background:var(--white);position:relative}
.abs{position:absolute}

/* brand concepts */
.concepts{left:0;top:0;width:1200px;height:218px}
.concepts .rule{left:4px;right:0;top:218px;height:1px;background:var(--blue-mid)}
.concept{display:flex;align-items:center;gap:14px;font-size:30px;font-weight:500}
.concept .dot{width:18px;height:18px;border-radius:50%;background:var(--blue)}
.concept.grey{color:var(--grey);left:248px;top:88px;font-size:38px}
.concept.grey .dot{background:var(--yellow);width:26px;height:26px}
.concept.a{left:586px;top:88px;color:var(--blue-deep);font-size:28px}
.concept.b{left:818px;top:92px;color:var(--blue-deep);font-size:28px}

/* header */
.site-header{left:0;top:219px;width:1200px;height:105px}
.brand{left:52px;top:252px;display:flex;align-items:center;gap:12px;color:var(--blue);font-size:24px;font-weight:500}
.brand .dot{width:22px;height:22px;border-radius:50%;background:var(--yellow)}
.main-nav{left:273px;top:282px;display:flex;gap:24px;font-size:13px}
.enquire{left:1046px;top:265px;width:124px;height:30px;border-radius:15px;background:var(--yellow);font-size:13px;display:flex;align-items:center;justify-content:center;color:var(--blue-deep)}

/* hero */
.hero{left:0;top:324px;width:1200px;height:518px;background:var(--blue-pale)}
.hero-kicker{left:122px;top:398px;font-size:36px;font-weight:700;color:var(--blue)}
.hero-title{left:125px;top:452px;font-size:36px;line-height:54px;font-weight:400;width:460px}
.hero-points{left:128px;top:636px;list-style:none;font-size:13px}
.hero-points li{display:flex;align-items:center;gap:8px;height:36px}
.hero-points svg{width:12px;height:12px}
.photo-back{left:861px;top:371px;width:212px;height:317px;background:linear-gradient(160deg,#c9d9ea,#8fa7bd)}
.photo-front{left:673px;top:466px;width:215px;height:329px;background:linear-gradient(160deg,#7a8fa3,#b88c4e)}

/* section heads */
.section-head{font-size:36px;line-height:45px;font-weight:400}

/* solutions */
.card{top:1017px;width:267px;height:369px;border-radius:4px;background:linear-gradient(180deg,#2d9be0 0%,#6e9cc2 40%,#3c5a78 75%,#23364a 100%);color:var(--white);overflow:hidden}
.card h3{position:absolute;left:26px;top:34px;font-size:18px;font-weight:400}
.card .rule{position:absolute;left:26px;right:16px;top:77px;height:1px;background:rgba(255,255,255,.35)}
.card h4{position:absolute;left:26px;top:206px;font-size:15px;font-weight:400}
.card ul{position:absolute;left:26px;top:243px;list-style:none;font-size:11.5px}
.card li{display:flex;align-items:center;gap:6px;height:22.5px}
.card li svg{width:10px;height:10px}
.card .btn{position:absolute;left:26px;top:326px;width:97px;height:29px;border-radius:15px;background:var(--yellow);color:var(--blue-deep);font-size:11px;display:flex;align-items:center;justify-content:center}

/* insights */
.feature{left:126px;top:1584px;width:432px;height:381px;background:linear-gradient(180deg,#d6dade,#7d8a96);color:var(--white)}
.feature p{position:absolute;left:20px;bottom:33px;width:390px;font-size:13px;line-height:16px}
.post{width:240px;height:188px;background:var(--blue-soft)}
.post .ph{height:142px;background:linear-gradient(150deg,#9db6cc,#4c6a88)}
.post p{padding:9px 12px;font-size:11.5px;line-height:14px}

/* stats */
.stat{top:2153px;width:197px;height:109px;border:1px solid var(--line);border-radius:4px;padding:22px 14px}
.stat b{display:block;font-size:18px;font-weight:400;color:var(--blue)}
.stat span{display:block;margin-top:22px;font-size:11.5px}

/* contact band */
.contact{left:0;top:2376px;width:1200px;height:607px;background:var(--blue);color:var(--white)}
.claim{left:124px;top:2470px;font-size:56px;line-height:76px;font-weight:400}
.claim em{font-style:normal;color:var(--yellow)}
.about{left:126px;top:2640px;width:430px;font-size:15px;line-height:22.6px}
.about strong{color:var(--yellow);font-weight:500}
.form-title{left:634px;top:2476px;font-size:22px}
.label{font-size:13px}
.field{width:203px;height:42px;border:1px solid var(--blue-soft);border-radius:4px}
.submit{left:893px;top:2758px;width:178px;height:37px;border-radius:19px;background:var(--yellow);color:var(--blue-deep);font-size:16px;display:flex;align-items:center;justify-content:center}

/* footer */
.footer-nav{left:54px;top:3016px;display:flex;gap:24px;font-size:13px}
.copyright{right:56px;top:3016px;font-size:13px}
</style>
</head>
<body>

<section class="abs concepts" aria-label="Brand concepts">
  <div class="abs concept grey"><span>LOGO</span><span class="dot"></span></div>
  <div class="abs concept a"><span class="dot"></span><span>Brightvale</span></div>
  <div class="abs concept b"><span class="dot"></span><span>Energy</span></div>
  <div class="abs rule"></div>
</section>

<header class="abs site-header"></header>
<div class="abs brand"><span class="dot"></span><span>Brightvale Energy</span></div>
<nav class="abs main-nav"><span>Solar PV</span><span>Battery Energy Storage</span><span>EV Charging</span><span>Heat Pumps</span><span>Contact us</span></nav>
<div class="abs enquire">Enquire Now</div>

<section class="abs hero"></section>
<div class="abs hero-kicker">BRIGHTVALE ENERGY</div>
<h1 class="abs hero-title">Delivering High-Quality Solar Energy Solutions to Households Across UK</h1>
<ul class="abs hero-points">
  <li><svg viewBox="0 0 12 12"><circle cx="6" cy="6" r="5" fill="none" stroke="#0677BA"/><path d="M3.5 6l1.8 1.8L8.6 4.4" fill="none" stroke="#0677BA"/></svg>Maximise your savings with powerful 465w solar panels.</li>
  <li><svg viewBox="0 0 12 12"><circle cx="6" cy="6" r="5" fill="none" stroke="#0677BA"/><path d="M3.5 6l1.8 1.8L8.6 4.4" fill="none" stroke="#0677BA"/></svg>Peace of mind with a 30 year performance guarantee.</li>
  <li><svg viewBox="0 0 12 12"><circle cx="6" cy="6" r="5" fill="none" stroke="#0677BA"/><path d="M3.5 6l1.8 1.8L8.6 4.4" fill="none" stroke="#0677BA"/></svg>Start saving quickly with installation in just 3 weeks.</li>
</ul>
<div class="abs photo-back" role="img" aria-label="Bright living room ceiling with window light"></div>
<div class="abs photo-front" role="img" aria-label="Couple relaxing at home with mugs of tea"></div>

<h2 class="abs section-head" style="left:52px;top:886px">Solutions<br>We Deliver</h2>

<article class="abs card" style="left:52px" role="img" aria-label="Installer carrying a solar panel">
  <h3>Solar PV</h3><div class="rule"></div><h4>Reduce bills</h4>
  <ul>
    <li><svg viewBox="0 0 10 10"><circle cx="5" cy="5" r="4.3" fill="none" stroke="#fff"/><path d="M3 5h4M5.5 3.5L7 5 5.5 6.5" fill="none" stroke="#fff"/></svg>Free workmanship guarantee.</li>
    <li><svg viewBox="0 0 10 10"><circle cx="5" cy="5" r="4.3" fill="none" stroke="#fff"/><path d="M3 5h4M5.5 3.5L7 5 5.5 6.5" fill="none" stroke="#fff"/></svg>Market leading 460w panels.</li>
    <li><svg viewBox="0 0 10 10"><circle cx="5" cy="5" r="4.3" fill="none" stroke="#fff"/><path d="M3 5h4M5.5 3.5L7 5 5.5 6.5" fill="none" stroke="#fff"/></svg>Premium 5kw to 15kw battery.</li>
  </ul>
  <div class="btn">Learn more</div>
</article>
<article class="abs card" style="left:328px" role="img" aria-label="Technician fitting a home battery unit">
  <h3>Battery Energy Storage</h3><div class="rule"></div><h4>Energy Independence</h4>
  <ul>
    <li><svg viewBox="0 0 10 10"><circle cx="5" cy="5" r="4.3" fill="none" stroke="#fff"/><path d="M3 5h4M5.5 3.5L7 5 5.5 6.5" fill="none" stroke="#fff"/></svg>Maximizes Solar Utilization.</li>
    <li><svg viewBox="0 0 10 10"><circle cx="5" cy="5" r="4.3" fill="none" stroke="#fff"/><path d="M3 5h4M5.5 3.5L7 5 5.5 6.5" fill="none" stroke="#fff"/></svg>Provides Backup Power &amp; Reliability.</li>
    <li><svg viewBox="0 0 10 10"><circle cx="5" cy="5" r="4.3" fill="none" stroke="#fff"/><path d="M3 5h4M5.5 3.5L7 5 5.5 6.5" fill="none" stroke="#fff"/></svg>Improves Return on Investment.</li>
  </ul>
  <div class="btn">Learn more</div>
</article>
<article class="abs card" style="left:603px" role="img" aria-label="Electric car connected to a wall charger">
  <h3>EV Charging</h3><div class="rule"></div><h4>Charge Your EV the Smart Way</h4>
  <ul>
    <li><svg viewBox="0 0 10 10"><circle cx="5" cy="5" r="4.3" fill="none" stroke="#fff"/><path d="M3 5h4M5.5 3.5L7 5 5.5 6.5" fill="none" stroke="#fff"/></svg>Drive on Sunshine, Save More.</li>
    <li><svg viewBox="0 0 10 10"><circle cx="5" cy="5" r="4.3" fill="none" stroke="#fff"/><path d="M3 5h4M5.5 3.5L7 5 5.5 6.5" fill="none" stroke="#fff"/></svg>Get More from Your Solar.</li>
    <li><svg viewBox="0 0 10 10"><circle cx="5" cy="5" r="4.3" fill="none" stroke="#fff"/><path d="M3 5h4M5.5 3.5L7 5 5.5 6.5" fill="none" stroke="#fff"/></svg>Be Ready for the Future of Mobility.</li>
  </ul>
  <div class="btn">Learn more</div>
</article>
<article class="abs card" style="left:879px;background:linear-gradient(180deg,#2d9be0 0%,#6e9cc2 25%,#2c4a78 45%,#4a5c4a 75%,#3f6b2e 100%)" role="img" aria-label="Heat pump unit beside a house with rooftop panels">
  <h3>Heat Pumps</h3><div class="rule"></div><h4>Heat your home efficiently.</h4>
  <ul>
    <li><svg viewBox="0 0 10 10"><circle cx="5" cy="5" r="4.3" fill="none" stroke="#fff"/><path d="M3 5h4M5.5 3.5L7 5 5.5 6.5" fill="none" stroke="#fff"/></svg>Leading GB manufacturer..</li>
    <li><svg viewBox="0 0 10 10"><circle cx="5" cy="5" r="4.3" fill="none" stroke="#fff"/><path d="M3 5h4M5.5 3.5L7 5 5.5 6.5" fill="none" stroke="#fff"/></svg>Free workmanship guarantee.</li>
    <li><svg viewBox="0 0 10 10"><circle cx="5" cy="5" r="4.3" fill="none" stroke="#fff"/><path d="M3 5h4M5.5 3.5L7 5 5.5 6.5" fill="none" stroke="#fff"/></svg>Government grant of £7,500.</li>
  </ul>
  <div class="btn">Learn more</div>
</article>

<h2 class="abs section-head" style="left:126px;top:1452px">Solar Insights<br>&amp; Updates</h2>

<article class="abs feature" role="img" aria-label="Two installers lifting a solar panel onto a roof">
  <p>Lorem ipsum dolor sit amet, consectetur adipiscing elit, sed do eiusmod tempor incididunt ut labore et dolore magna aliqua.</p>
</article>
<article class="abs post" style="left:575px;top:1584px"><div class="ph" role="img" aria-label="Electrician wiring an inverter"></div><p>Lorem ipsum dolor sit amet, consectetur adipiscing elit.</p></article>
<article class="abs post" style="left:830px;top:1584px"><div class="ph" role="img" aria-label="Family looking at solar panels"></div><p>Lorem ipsum dolor sit amet, consectetur adipiscing elit.</p></article>
<article class="abs post" style="left:575px;top:1783px"><div class="ph" role="img" aria-label="Installer holding a solar panel"></div><p>Lorem ipsum dolor sit amet, consectetur adipiscing elit.</p></article>
<article class="abs post" style="left:830px;top:1783px"><div class="ph" role="img" aria-label="Workers fitting panels on a tiled roof"></div><p>Lorem ipsum dolor sit amet, consectetur adipiscing elit.</p></article>

<h2 class="abs section-head" style="left:52px;top:2024px">100% Ready to<br>be Your Partner</h2>

<div class="abs stat" style="left:52px"><b>10,000+</b><span>Customers Served Nationwide</span></div>
<div class="abs stat" style="left:257px;padding-left:22px"><b>100%</b><span>Renewable Energy Solutions</span></div>
<div class="abs stat" style="left:462px;padding-left:20px"><b>10 +</b><span>Years of Industry Experience</span></div>
<div class="abs stat" style="left:668px;padding-left:20px"><b>30</b><span>Years Performance Guarantee</span></div>
<div class="abs stat" style="left:874px;padding-left:24px"><b>98%</b><span>Customer Retention Rate</span></div>

<section class="abs contact"></section>
<h2 class="abs claim" style="color:#fff">Clear Benefits<br>No <em>Hidden</em> Fees.</h2>
<p class="abs about" style="color:#fff"><strong>Brightvale Energy International Ltd</strong> is a UK-based renewable energy company delivering high-quality solar energy solutions to households across the country. Through its franchise model under the consumer-facing brand "Brightvale Energy," the company is leading the charge in sustainable energy deployment, contributing to the UK's Net Zero Annual Energy Target of 70GW of power by 2035, while offering a robust business opportunity for aspiring franchisees.</p>
<div class="abs form-title" style="color:#fff">Let’s build something better together.</div>
<div class="abs label" style="left:634px;top:2548px;color:#fff">First Name</div>
<div class="abs label" style="left:868px;top:2548px;color:#fff">First Name</div>
<div class="abs field" style="left:634px;top:2578px"></div>
<div class="abs field" style="left:868px;top:2578px"></div>
<div class="abs label" style="left:634px;top:2646px;color:#fff">Email</div>
<div class="abs label" style="left:868px;top:2646px;color:#fff">Phone Number</div>
<div class="abs field" style="left:634px;top:2676px"></div>
<div class="abs field" style="left:868px;top:2676px"></div>
<div class="abs submit">Get consultation</div>

<nav class="abs footer-nav"><span>Home</span><span>Solar PV</span><span>Battery Energy Storage</span><span>EV Charging</span><span>Heat Pumps</span><span>Contact us</span></nav>
<div class="abs copyright">Copyright © Brightvale Energy 2025. All Right Reserved.</div>

</body>
</html>
```